Delicious packaging for custom chocolate bars

The customer will create their own custom chocolate bar from over 70 different ingredients- fruit, nuts and sweets.

The bars will be sealed in cellophane bags and then placed in an envelope with a large window which allows the toppings on the chocolate bar to be seen.

The packaging should be appealing and attractive to suit the gift market- so looking quite premium/artisan, but also a bit unique and quirky.

Am currently looking for one base design, but in the future am looking to offer several packaging design variations that the customer can select from (for example, seasonal ones).

Reason: hi i have committed to pay for this projectnow and am extending the day as i would like to get some more designers providing their ideas. Thanks!

Target Market(s)

Gift purchasers; Australian females 15-39 years old, foodies/gourmet food lovers

Requirements
Must have
• 1) Design for a DLX sized envelope
- Including a window
- Base design to have a blank space to allow for application of label (label will be customised for each order)
- Website url to be prominent (crunvelo.com.au)

2) Design for label that can be printed individually (intending to thermal print from a PC) and will fit in the space allowed for on the envelope. Label needs to contain
- Printing on label will be in black, and background will be white
- Product name/message field (which will have been selected by the customer)
- Listing of the ingredients the customer selected (up to 5- for example as a bullet pointed list)
- Standard Australian Nutrition panel
- Additional required text as per attachment which will be loaded up
Nice to have
• 1) Would like the files in SVG format if possible?

2) Would like the window to be a reasonable size so the contents are quite visible- was thinking about 80mmX80mm or equivalent (doesn't have to be square though)

4) Would like a design that integrates the separate label well- for example it could be placed on an area which has a white background and a larger border/shape around it. Also, because the label will have a mix of "important" stuff (like the name the customer has selected for the mix) and more boring stuff (like the nutrition panel & contact details)- it could make sense for the label to be located running over from front to back of the envelope- with nutrition panel ending up on the back and the name on the front.

3) Base stock for the envelope could be kraft brown. I also like the idea of an image of a ribbon or bow to give a little bit of personality and look "gifty"

```html
<!DOCTYPE html>
<html lang="en">
<head>
<meta charset="utf-8">
<title>Crunvelo – Birthday Bar Envelope</title>
<link rel="stylesheet" href="https://fonts.googleapis.com/css2?family=Lobster&family=Lobster+Two:wght@700&family=Federo&display=swap">
<style>
  :root {
    --envelope-black: #020109;
    --gold: #c9a04f;
    --label-white: #ffffff;
    --ink: #0b0a1e;
    --stripe: #ffffff;
    --choc-light: #a88489;
    --choc-mid: #9a7478;
    --choc-dark: #7f5653;
  }
  html, body {
    margin: 0;
    padding: 0;
    width: 1200px;
    height: 2475px;
    overflow: hidden;
    background: var(--envelope-black);
  }
  .envelope {
    position: relative;
    width: 1200px;
    height: 2475px;
    background: var(--envelope-black);
    overflow: hidden;
  }
  .stripe {
    position: absolute;
    left: 0;
    width: 100%;
    height: 5px;
    background: var(--stripe);
  }
  .label-band {
    position: absolute;
    left: 4px;
    right: 4px;
    top: 155px;
    height: 586px;
    background: var(--gold);
  }
  .label {
    position: absolute;
    left: 0;
    right: 0;
    top: 42px;
    height: 501px;
    background: var(--label-white);
    text-align: center;
    color: var(--ink);
  }
  .label-title {
    margin: 0;
    padding-top: 42px;
    font-family: "Lobster Two", cursive;
    font-weight: 700;
    font-size: 112px;
    line-height: 108px;
    letter-spacing: 1px;
  }
  .ingredients {
    list-style: none;
    margin: 30px 0 0;
    padding: 0;
    font-family: "Federo", sans-serif;
    font-size: 52px;
    line-height: 76px;
  }
  .ingredients li {
    display: inline-block;
    margin: 0 34px;
  }
  .ingredients li::before {
    content: "•";
    font-size: 34px;
    margin-right: 20px;
    vertical-align: middle;
  }
  .brand-name {
    position: absolute;
    left: 0;
    right: 0;
    top: 770px;
    margin: 0;
    text-align: center;
    font-family: "Lobster", cursive;
    font-weight: 400;
    font-size: 158px;
    line-height: 190px;
    color: var(--gold);
  }
  .window {
    position: absolute;
    left: 122px;
    top: 1020px;
    width: 977px;
    height: 1299px;
  }
  .window svg { display: block; }
</style>
</head>
<body>
<main class="envelope">
  <div class="stripe" style="top:4px"></div>
  <div class="stripe" style="top:24px"></div>
  <div class="stripe" style="top:42px"></div>

  <section class="label-band">
    <div class="label">
      <h1 class="label-title">Marcus’s<br>Birthday Bar</h1>
      <ul class="ingredients">
        <li>Dark Chocolate</li><li>Walnuts</li><br>
        <li>Coffee</li><li>Ginger</li>
      </ul>
    </div>
  </section>

  <p class="brand-name">Crunvelo</p>

  <div class="window">
    <svg width="977" height="1299" viewBox="0 0 977 1299">
      <defs>
        <linearGradient id="chocolate" x1="0" y1="0" x2="1" y2="1">
          <stop offset="0" stop-color="var(--choc-light)"/>
          <stop offset="0.5" stop-color="var(--choc-mid)"/>
          <stop offset="1" stop-color="var(--choc-dark)"/>
        </linearGradient>
      </defs>
      <path class="window-frame" fill="var(--gold)"
        d="M64 0 H913 A64 64 0 0 0 977 64 V1235 A64 64 0 0 0 913 1299 H64 A64 64 0 0 0 0 1235 V64 A64 64 0 0 0 64 0 Z"/>
      <path class="window-bar" role="img" aria-label="Chocolate bar with squared segments seen through the window"
        fill="url(#chocolate)"
        d="M90 26 H887 A64 64 0 0 0 951 90 V1209 A64 64 0 0 0 887 1273 H90 A64 64 0 0 0 26 1209 V90 A64 64 0 0 0 90 26 Z"/>
    </svg>
  </div>

  <div class="stripe" style="top:2413px"></div>
  <div class="stripe" style="top:2436px"></div>
  <div class="stripe" style="top:2462px"></div>
</main>
</body>
</html>
```